Personal Vistrano Banner

I am creating a personal brand for myself. I want a vistrano banner that inspires and motivates people to reach their epic awesomeness. I am creating and designing my personal brand. It can be a background with words on a scenery a picture or 3d graphic. If someone looked at it, they should say it is aggressively epic and motivating. It should be dramatic and bold.
My personal goal is to help as many people reach financial freedom as possible, and challenge and break their own limiting beliefs. This personal brand will be integrated into my zomblat, quorVex, and professional vistrano fanpage (in addition to personal page). My goals are to open up a school for the underpriveleged children, develop my network marketing company team, and become a billionaire in the process. I want to attract people to me that really identify with doing what most think is impossible in terms of personal growth, impact to the world and financial wealth.
Updates

I have updated my brief with more background, and added a new comment to the discussion section to give you more to work with.

Reason: To give designers more time and to create a second and third place prize.

Reason: I am giving designers time to submit more designs

Target Market(s)

business professionals, and people with an entrepreneurial spirit.

Industry/Entity Type

Financial

Requirements
Must have
• It must be the exact dimensions required for vistrano banners. It should not be bigger or smaller. exact!!!

```html
<!DOCTYPE html>
<html lang="en">
<head>
<meta charset="utf-8">
<title>Your Brand – Vistrano Page</title>
<link rel="stylesheet" href="https://fonts.googleapis.com/css2?family=Roboto:wght@400;500;700&family=Baloo+2:wght@700;800&display=swap">
<style>
  :root {
    --page-bg: #e9ebf2;
    --bar-top: #5069a2;
    --bar-bottom: #3b5795;
    --bar-edge: #2f4677;
    --bar-text: #d6deee;
    --white: #ffffff;
    --ink: #1c2a47;
    --muted: #6d7486;
    --link: #3b5998;
    --panel: #f0f2f7;
    --line: #c9cfdc;
    --tile: #7a7a7a;
    --tile-num: #959595;
    --rail: #d3d8e5;
    --rail-active: #6d7fae;
    --rail-text: #7c8bb3;
    --sky-top: #86abc6;
    --sky-mid: #c4d7e3;
    --sky-low: #dde7ee;
    --trees: #44702f;
    --headline: #eef4f8;
  }
  * { box-sizing: border-box; margin: 0; padding: 0; }
  html, body { width: 1200px; height: 559px; overflow: hidden; }
  body {
    position: relative;
    background: var(--page-bg);
    font-family: "Roboto", Arial, sans-serif;
    color: var(--ink);
  }
  .abs { position: absolute; }

  /* top navigation */
  .top-bar {
    left: 0; top: 0; width: 1200px; height: 41px;
    background: linear-gradient(var(--bar-top), var(--bar-bottom));
    border-bottom: 1px solid var(--bar-edge);
  }
  .brand-name { left: 146px; top: 13px; font-size: 12px; font-weight: 700; color: var(--white); }
  .search {
    left: 200px; top: 9px; width: 524px; height: 22px;
    background: var(--white); border: 1px solid var(--bar-edge);
    font-size: 14px; line-height: 20px; padding-left: 6px; color: #111;
  }
  .search svg { position: absolute; right: 6px; top: 4px; }
  .nav-icons { left: 846px; top: 10px; }
  .nav-link { top: 13px; font-size: 11px; font-weight: 700; color: var(--bar-text); }
  .nav-tools { left: 1034px; top: 13px; }

  /* main column */
  .page-card {
    left: 144px; top: 42px; width: 805px; height: 473px;
    background: var(--white); border: 1px solid var(--line); border-top: none;
  }
  .cover {
    left: 144px; top: 42px; width: 805px; height: 295px;
    background:
      linear-gradient(to top, var(--trees) 0%, rgba(68,112,47,0.85) 12%, rgba(68,112,47,0) 32%),
      linear-gradient(var(--sky-top), var(--sky-mid) 50%, var(--sky-low) 75%);
    overflow: hidden;
  }
  .cover-headline {
    left: 30px; top: 14px;
    font-family: "Baloo 2", "Trebuchet MS", sans-serif; font-weight: 800;
    color: var(--headline); font-size: 38px; line-height: 1;
    white-space: nowrap;
  }
  .cover-headline .epic { font-size: 62px; letter-spacing: 1px; }

  .profile-frame {
    left: 166px; top: 239px; width: 160px; height: 159px;
    background: var(--white); border: 1px solid #9aa3b6; border-radius: 3px;
  }
  .page-name { left: 339px; top: 353px; font-size: 18px; font-weight: 700; color: var(--ink); }
  .page-stats { left: 339px; top: 376px; font-size: 10px; color: var(--muted); }

  .button {
    height: 23px; top: 354px;
    background: linear-gradient(#fafafa, #e7e8ec);
    border: 1px solid #9a9fab; border-radius: 2px;
    font-size: 12px; font-weight: 700; color: #333;
    display: flex; align-items: center; padding: 0 8px; gap: 5px;
  }
  .button-liked { left: 739px; width: 65px; }
  .button-message { left: 814px; width: 111px; padding: 0; }
  .button-message .label { padding: 0 8px; border-right: 1px solid #b9bdc7; height: 100%; display: flex; align-items: center; }
  .button-message .gear { padding: 0 6px; display: flex; align-items: center; gap: 4px; }

  .about-panel {
    left: 145px; top: 410px; width: 309px; height: 70px;
    background: var(--panel); border: 1px solid #dde1ea;
    padding: 6px 0 0 24px; font-size: 10px; line-height: 15px;
  }
  .about-panel .category { color: var(--muted); }
  .about-panel .blurb { color: #222; }
  .about-panel a { color: var(--link); text-decoration: none; }
  .about-links { left: 185px; top: 483px; font-size: 10px; color: var(--link); }

  .tile {
    top: 410px; width: 106px; height: 70px; background: var(--tile);
    border: 1px solid #6a6a6a;
    display: flex; align-items: center; justify-content: center;
    font-size: 40px; font-weight: 700; color: var(--tile-num);
  }
  .tile-likes { background: var(--panel); border-color: #dde1ea; color: var(--ink); font-size: 21px; gap: 5px; }
  .tile-likes .mark { width: 14px; height: 14px; background: var(--link); border-radius: 2px; }
  .tile-label { top: 487px; font-size: 10px; color: var(--link); }
  .tile-strip { left: 913px; top: 410px; width: 35px; height: 70px; background: var(--panel); border: 1px solid #dde1ea; }
  .tile-more {
    left: 910px; top: 437px; width: 27px; height: 15px; background: var(--white);
    border: 1px solid #9aa3b6; font-size: 10px; color: #444;
    display: flex; align-items: center; justify-content: center; gap: 2px;
  }

  /* timeline spine */
  .spine { left: 546px; top: 515px; width: 3px; height: 44px; background: var(--rail); }
  .highlights {
    left: 506px; top: 530px; width: 82px; height: 22px;
    background: var(--panel); border: 1px solid #bfc6d6; border-radius: 2px;
    font-size: 10px; color: #7d87a3;
    display: flex; align-items: center; justify-content: center; gap: 5px;
  }

  /* year navigation */
  .year-rail { left: 960px; top: 43px; list-style: none; }
  .year-rail li {
    height: 21.8px; line-height: 21.8px; padding-left: 10px;
    border-left: 4px solid var(--rail);
    font-size: 10.5px; color: var(--rail-text);
  }
  .year-rail li.is-current { border-left-color: var(--rail-active); font-weight: 700; color: #5a6c9c; }
</style>
</head>
<body>

<header class="abs top-bar">
  <span class="abs brand-name">Vistrano</span>
  <div class="abs search">Your Brand
    <svg width="12" height="12" viewBox="0 0 12 12"><circle cx="5" cy="5" r="3.8" fill="none" stroke="#777" stroke-width="1.4"/><line x1="8" y1="8" x2="11" y2="11" stroke="#777" stroke-width="1.6"/></svg>
  </div>
  <svg class="abs nav-icons" width="72" height="20" viewBox="0 0 72 20">
    <g fill="#2c4173">
      <circle cx="6" cy="6" r="3.5"/><path d="M0 17c0-5 12-5 12 0z"/>
      <circle cx="13" cy="6" r="3.5"/><path d="M7 17c0-5 12-5 12 0z"/>
      <path d="M27 3h16v10h-9l-4 4v-4h-3z"/>
      <circle cx="62" cy="10" r="8"/>
    </g>
  </svg>
  <span class="abs nav-link" style="left:944px">Home</span>
  <span class="abs nav-link" style="left:991px">Milo</span>
  <svg class="abs nav-tools" width="38" height="14" viewBox="0 0 38 14">
    <g fill="#c4cde2">
      <rect x="0" y="4" width="7" height="7"/><path d="M1.5 4V2.5a2 2 0 0 1 4 0V4" fill="none" stroke="#c4cde2" stroke-width="1.3"/>
      <rect x="8" y="4" width="6" height="1.4"/><rect x="8" y="7" width="6" height="1.4"/><rect x="8" y="10" width="6" height="1.4"/>
      <circle cx="31" cy="7" r="3.2"/><circle cx="31" cy="7" r="5" fill="none" stroke="#c4cde2" stroke-width="2" stroke-dasharray="2 1.9"/>
    </g>
  </svg>
</header>

<main>
  <section class="abs page-card"></section>

  <div class="abs cover" role="img" aria-label="Cover photo: a man in a dark suit seen from behind, arms spread wide toward a bright cloudy sky above green treetops">
    <h1 class="abs cover-headline">Release your <span class="epic">EPIC</span></h1>
  </div>

  <div class="abs profile-frame"></div>

  <h2 class="abs page-name">Your Brand</h2>
  <p class="abs page-stats">21,942,038 likes · 344,909 talking about this · 4,499,542 were here</p>

  <div class="abs button button-liked">
    <svg width="9" height="8" viewBox="0 0 9 8"><path d="M1 4l2.5 2.5L8 1" fill="none" stroke="#444" stroke-width="1.6"/></svg>Liked
  </div>
  <div class="abs button button-message">
    <span class="label">Message</span>
    <span class="gear">
      <svg width="10" height="10" viewBox="0 0 10 10"><circle cx="5" cy="5" r="2" fill="#333"/><circle cx="5" cy="5" r="3.6" fill="none" stroke="#333" stroke-width="1.8" stroke-dasharray="1.6 1.2"/></svg>
      <svg width="8" height="5" viewBox="0 0 8 5"><path d="M0 0h8L4 5z" fill="#555"/></svg>
    </span>
  </div>

  <div class="abs about-panel">
    <p class="category">Product/Service</p>
    <p class="blurb">Our product is awesome... Try it</p>
    <a href="#">http://lumenwarex.com/</a>
  </div>
  <p class="abs about-links">About – Suggest an Edit</p>

  <div class="abs tile" style="left:462px">1</div>
  <div class="abs tile" style="left:574px">2</div>
  <div class="abs tile tile-likes" style="left:687px"><span class="mark"></span>21m</div>
  <div class="abs tile" style="left:800px">4</div>
  <div class="abs tile-strip"></div>
  <div class="abs tile-more">3 <svg width="7" height="4" viewBox="0 0 7 4"><path d="M0 0h7L3.5 4z" fill="#3b5998"/></svg></div>

  <span class="abs tile-label" style="left:462px">Photos</span>
  <span class="abs tile-label" style="left:574px">Videos</span>
  <span class="abs tile-label" style="left:687px">Likes</span>
  <span class="abs tile-label" style="left:800px">Events</span>

  <div class="abs spine"></div>
  <div class="abs highlights">Highlights <svg width="7" height="4" viewBox="0 0 7 4"><path d="M0 0h7L3.5 4z" fill="#8a93ad"/></svg></div>
</main>

<nav>
  <ul class="abs year-rail">
    <li class="is-current">Recent</li>
    <li>2013</li><li>2012</li><li>2011</li><li>2010</li><li>2009</li>
    <li>2008</li><li>2006</li><li>2004</li><li>2003</li><li>2001</li>
    <li>2000</li><li>1998</li><li>1997</li><li>1996</li><li>1995</li>
    <li>1992</li><li>1997</li><li>1988</li><li>1987</li><li>1984</li>
    <li>1983</li><li>1982</li><li>Opened</li>
  </ul>
</nav>

</body>
</html>
```